Business Card Design Project

Maid Cleaning Services
Tidy Haven Cleaning Services
5550147268
tidyhavencleaning@examplemail.test
facebook - tidy haven

Business

We would really like a card that the shape of a made.
That would be great.
I would love to see how that would look.

```html
<!DOCTYPE html>
<html lang="en">
<head>
<meta charset="utf-8">
<title>Tidy Haven Cleaning Services – Business Cards</title>
<link href="https://fonts.googleapis.com/css2?family=Lato:wght@400;700&display=swap" rel="stylesheet">
<style>
  :root {
    --backdrop: #2b2b2d;
    --card: #ffffff;
    --ink: #1f1f1f;
    --brand-blue: #1f8fd0;
    --brand-green: #6cc04a;
    --faint: #eef5fa;
    --shadow: rgba(0, 0, 0, 0.45);
  }
  * { margin: 0; padding: 0; box-sizing: border-box; }
  html, body {
    width: 1200px;
    height: 880px;
    overflow: hidden;
    background: var(--backdrop);
    font-family: "Lato", Arial, sans-serif;
  }
  .canvas {
    position: relative;
    width: 1200px;
    height: 880px;
  }
  .card {
    position: absolute;
    width: 560px;
    height: 320px;
    background: var(--card);
    box-shadow: 0 12px 28px var(--shadow);
    overflow: hidden;
  }
  .card--front { left: 80px; top: 80px; }
  .card--back { left: 560px; top: 480px; }

  .brand-lockup {
    position: absolute;
    display: flex;
    align-items: center;
    gap: 12px;
  }
  .brand-lockup__dot {
    flex: none;
    border-radius: 50%;
    background: var(--brand-blue);
  }
  .brand-lockup__name {
    font-weight: 700;
    color: var(--brand-blue);
    line-height: 1.1;
  }
  .card--front .brand-lockup {
    left: 50%;
    top: 50%;
    transform: translate(-50%, -50%);
  }
  .card--front .brand-lockup__dot { width: 44px; height: 44px; }
  .card--front .brand-lockup__name { font-size: 30px; }

  .card--back .brand-lockup { right: 30px; top: 34px; }
  .card--back .brand-lockup__dot { width: 30px; height: 30px; }
  .card--back .brand-lockup__name { font-size: 21px; }

  .faint-mark {
    position: absolute;
    left: 40px;
    top: 40px;
    width: 240px;
    height: 240px;
    border-radius: 50%;
    background: var(--faint);
  }

  .contact {
    position: absolute;
    left: 34px;
    bottom: 34px;
    color: var(--ink);
  }
  .contact__company {
    font-size: 23px;
    font-weight: 400;
    margin-bottom: 14px;
  }
  .contact__list { list-style: none; }
  .contact__item {
    display: flex;
    align-items: center;
    gap: 10px;
    font-size: 15px;
    line-height: 1;
    margin-top: 6px;
  }
  .contact__icon {
    flex: none;
    width: 20px;
    height: 20px;
  }
</style>
</head>
<body>
<main class="canvas">

  <section class="card card--front" aria-label="Business card front">
    <div class="brand-lockup">
      <span class="brand-lockup__dot"></span>
      <span class="brand-lockup__name">Tidy Haven<br>Cleaning Services</span>
    </div>
  </section>

  <section class="card card--back" aria-label="Business card back">
    <div class="faint-mark" role="img" aria-label="Faint brand decoration"></div>

    <div class="brand-lockup">
      <span class="brand-lockup__dot"></span>
      <span class="brand-lockup__name">Tidy Haven<br>Cleaning Services</span>
    </div>

    <div class="contact">
      <p class="contact__company">Tidy Haven Cleaning Services</p>
      <ul class="contact__list">
        <li class="contact__item">
          <svg class="contact__icon" viewBox="0 0 20 20" aria-hidden="true">
            <circle cx="10" cy="10" r="9.5" fill="var(--brand-green)"/>
            <rect x="6.8" y="4.5" width="6.4" height="11" rx="1.2" fill="none" stroke="#fff" stroke-width="1.3"/>
            <circle cx="10" cy="13.6" r="0.8" fill="#fff"/>
          </svg>
          5550147268
        </li>
        <li class="contact__item">
          <svg class="contact__icon" viewBox="0 0 20 20" aria-hidden="true">
            <circle cx="10" cy="10" r="9.5" fill="var(--brand-green)"/>
            <rect x="5" y="6.5" width="10" height="7" rx="0.8" fill="none" stroke="#fff" stroke-width="1.3"/>
            <polyline points="5.3,7 10,11 14.7,7" fill="none" stroke="#fff" stroke-width="1.3"/>
          </svg>
          tidyhavencleaning@examplemail.test
        </li>
        <li class="contact__item">
          <svg class="contact__icon" viewBox="0 0 20 20" aria-hidden="true">
            <circle cx="10" cy="10" r="9.5" fill="var(--brand-green)"/>
          </svg>
          tidy haven
        </li>
      </ul>
    </div>
  </section>

</main>
</body>
</html>
```